Letterhead for Midwest Law Firm

Our law firm does estate planning and trust administration in Wisconsin and Illinois. We recently obtained a new logo and need to incorporate it into new stationary. The stationary needs to list out the attorneys at the firm, but we will want 3 variations, one with three attorneys, one with six, and one with six plus the names of states where each is licensed to practice (possibly as an asterisk with notation somewhere towards bottom of page. As with most traditional law practices, letterhead should be conservative and convey predictability and reliability. We view our brand as being primarily reliability, with prestige as a secondary element. We are upmarket, but would like to avoid seeming pretentious or "slick". We are a smaller firm with a personal touch.

Target Market(s)

Affluent Midwestern Americans approaching at or approaching retirement age.

Industry/Entity Type

Legal

Font styles to use
Serif
Sans Serif

Requirements
Must have
• Must use our logo. Must comply with Northgate Counsel Guild Ethics rules: https://www.quarvenlex.org/rules/offices/docs/plmtk41annotated.pdf. Must be conventional. Must list names of attorneys and provide contact information for firm. Note that we are asking for three designs with very minor variations. Also, designer must provide letterhead in a format that is industry-standard for stationary printers.
Nice to have
• We would appreciate an alternate version that will look reasonable when printed on a black-and-white printer. Designer can use judgment as to whether to have use grayscale, black/white, or something in between.
Should not have
• No "motto" or "visit our website" extraneous materials. putting the website address somewhere is fine, but overall there is a lot of required text, and we'd like to not appear cluttered.

```html
<!DOCTYPE html>
<html lang="en">
<head>
<meta charset="utf-8">
<title>Halvorsen &amp; Brandt LLP — Letterhead Variations</title>
<link href="https://fonts.googleapis.com/css2?family=Source+Sans+3:wght@300;400&family=Questrial&display=swap" rel="stylesheet">
<style>
  :root {
    --backdrop: #b1afb0;
    --paper: #f6f3f3;
    --ink: #2b2d3a;
    --navy: #2a2f52;
    --gold: #f2b233;
    --rule: #6b6b6b;
    --sky: #5ab3e0;
    --orange: #f27b2a;
    --green: #4cb050;
    --magenta: #e23fd0;
    --signature: #d9d6d8;
  }
  * { margin: 0; padding: 0; box-sizing: border-box; }
  html, body { width: 1200px; height: 580px; overflow: hidden; background: var(--backdrop); }
  body { position: relative; font-family: "Source Sans 3", sans-serif; color: var(--ink); }

  .letterhead {
    position: absolute; top: 67px; width: 330px; height: 465px;
    background: var(--paper);
    box-shadow: 1px 1px 2px rgba(0,0,0,.25);
  }
  .letterhead--three { left: 65px; }
  .letterhead--six { left: 437px; }
  .letterhead--offices { left: 809px; }

  .brand {
    position: absolute; top: 38px; left: 0; right: 0;
    display: flex; justify-content: center; align-items: center; gap: 5px;
  }
  .letterhead--offices .brand { top: 42px; }
  .brand-dot { width: 9px; height: 9px; border-radius: 50%; background: var(--gold); }
  .brand-name { font-size: 9px; font-weight: 400; color: var(--navy); letter-spacing: .1px; }

  .salutation { position: absolute; top: 129px; left: 33px; font-size: 8.8px; font-weight: 300; }

  .body-copy { position: absolute; top: 156px; left: 33px; width: 266px; }
  .body-copy p {
    font-size: 5.75px; line-height: 7.9px; font-weight: 400; text-align: justify; margin-bottom: 7.9px;
  }

  .closing { position: absolute; top: 323px; left: 33px; font-size: 5.3px; }
  .signature {
    position: absolute; top: 340px; left: 33px; width: 43px; height: 17px;
    background: var(--signature); border-radius: 2px;
  }

  .attorneys { position: absolute; left: 33px; font-family: "Questrial", sans-serif; list-style: none; }
  .letterhead--three .attorneys { top: 426px; font-size: 6px; line-height: 7.6px; }
  .letterhead--six .attorneys { top: 409px; font-size: 5px; line-height: 6.3px; }
  .letterhead--offices .attorneys { top: 394px; left: 36px; font-size: 4.8px; line-height: 6.65px; }

  .star { margin-right: 1.5px; }
  .star--gold { color: var(--gold); }
  .star--sky { color: var(--sky); }
  .star--orange { color: var(--orange); }
  .star--green { color: var(--green); }
  .star--magenta { color: var(--magenta); }
  .star--navy { color: var(--navy); }

  .contact {
    position: absolute; right: 31px; text-align: right; font-style: normal;
    font-family: "Questrial", sans-serif; font-size: 5.6px; line-height: 7.6px;
  }
  .letterhead--three .contact, .letterhead--six .contact { top: 426px; }
  .letterhead--offices .contact { top: 413px; right: 33px; font-size: 5.4px; line-height: 7.2px; }
  .contact-label { font-weight: 700; }

  .office-rule {
    position: absolute; top: 437px; left: 37px; width: 260px; height: 0;
    border-top: .6px solid var(--rule);
  }
  .offices {
    position: absolute; top: 440px; left: 0; right: 0; text-align: center;
    font-family: "Questrial", sans-serif; font-size: 5.6px; list-style: none;
  }
  .offices li { display: inline; margin: 0 1.2px; }
</style>
</head>
<body>

<!-- Variation 1: three attorneys -->
<section class="letterhead letterhead--three">
  <header class="brand"><span class="brand-dot"></span><span class="brand-name">Halvorsen &amp; Brandt LLP</span></header>
  <p class="salutation">Dear Mr. Smith,</p>
  <div class="body-copy">
    <p>Lorem ipsum dolor sit amet, consectetur adipiscing elit. Donec orci purus, luctus vitae dignissim eu, iaculis sed purus. Vivamus faucibus, ipsum nec aliquet viverra, leo mauris condimentum ligula, sit amet sagittis enim ligula quis arcu. Nam egestas tortor id nisi porttitor mattis. In tortor ante, ultricies in suscipit a, tempus non massa. Vivamus et auctor mi. Fusce vel massa nulla. Phasellus nec eros mauris, et scelerisque orci.</p>
    <p>Donec malesuada orci vitae nulla accumsan porta a id massa. Quisque accumsan iaculis magna sit amet fringilla. Maecenas consequat, magna eget tincidunt semper, odio nibh rutrum mi, id feugiat ante nisi eu risus. Vestibulum nunc orci, rhoncus a placerat in, ultricies in mi. Cras mattis varius eros, vel fringilla nisi suscipit eget. Quisque scelerisque sagittis nulla at porttitor.</p>
    <p>Sed id augue vitae urna euismod commodo aliquet a quam. Pellentesque arcu velit, cursus et malesuada ut, consequat et diam. Nullam erat sem, rhoncus id ullamcorper vitae, rhoncus et arcu. In ultricies ultricies nulla, ut rutrum nisi iaculis at. Donec eu magna a metus ornare faucibus. Fusce aliquet faucibus ultricies. Morbi semper, est id tincidunt gravida, sem arcu adipiscing lacus, ac bibendum nulla leo eu purus. Quisque nec diam sed risus consectetur a ccumsan quis quis nibh. Vestibulum id purus lorem.</p>
    <p>It is a long established fact that a reader will be distracted by the readable content of a page when looking at its layout. The point of using Lorem Ipsum is that it has a more-or-less normal distribution of letters, as opposed to using 'Content here, content here', making it look like readable English. Many desktop publishing packages</p>
  </div>
  <p class="closing">Sincerely,</p>
  <div class="signature" role="img" aria-label="Handwritten signature of the attorney"></div>
  <ul class="attorneys">
    <li>Daniel P. Halvorsen</li>
    <li>Thomas E. Brandt</li>
    <li>Walter K. Halvorsen</li>
  </ul>
  <address class="contact">218 W. Larchmont Street<br>Suite 300, Alderton, WI 53210<br>P. 414-555-0148&nbsp; F. 414-555-0192</address>
</section>

<!-- Variation 2: six attorneys -->
<section class="letterhead letterhead--six">
  <header class="brand"><span class="brand-dot"></span><span class="brand-name">Halvorsen &amp; Brandt LLP</span></header>
  <p class="salutation">Dear Mr. Smith,</p>
  <div class="body-copy">
    <p>Lorem ipsum dolor sit amet, consectetur adipiscing elit. Donec orci purus, luctus vitae dignissim eu, iaculis sed purus. Vivamus faucibus, ipsum nec aliquet viverra, leo mauris condimentum ligula, sit amet sagittis enim ligula quis arcu. Nam egestas tortor id nisi porttitor mattis. In tortor ante, ultricies in suscipit a, tempus non massa. Vivamus et auctor mi. Fusce vel massa nulla. Phasellus nec eros mauris, et scelerisque orci.</p>
    <p>Donec malesuada orci vitae nulla accumsan porta a id massa. Quisque accumsan iaculis magna sit amet fringilla. Maecenas consequat, magna eget tincidunt semper, odio nibh rutrum mi, id feugiat ante nisi eu risus. Vestibulum nunc orci, rhoncus a placerat in, ultricies in mi. Cras mattis varius eros, vel fringilla nisi suscipit eget. Quisque scelerisque sagittis nulla at porttitor.</p>
    <p>Sed id augue vitae urna euismod commodo aliquet a quam. Pellentesque arcu velit, cursus et malesuada ut, consequat et diam. Nullam erat sem, rhoncus id ullamcorper vitae, rhoncus et arcu. In ultricies ultricies nulla, ut rutrum nisi iaculis at. Donec eu magna a metus ornare faucibus. Fusce aliquet faucibus ultricies. Morbi semper, est id tincidunt gravida, sem arcu adipiscing lacus, ac bibendum nulla leo eu purus. Quisque nec diam sed risus consectetur a ccumsan quis quis nibh. Vestibulum id purus lorem.</p>
    <p>It is a long established fact that a reader will be distracted by the readable content of a page when looking at its layout. The point of using Lorem Ipsum is that it has a more-or-less normal distribution of letters, as opposed to using 'Content here, content here', making it look like readable English. Many desktop publishing packages</p>
  </div>
  <p class="closing">Sincerely,</p>
  <div class="signature" role="img" aria-label="Handwritten signature of the attorney"></div>
  <ul class="attorneys">
    <li>Thomas E. Brandt</li>
    <li>Walter K. Halvorsen</li>
    <li>Gregory L. Kowalczyk, SR. Associate</li>
    <li>Laura M. Rourke, SR. Associate</li>
    <li>Karen E. Lindqvist,&nbsp; SR. Associate</li>
    <li>Diane F. Thorsby, Associate</li>
  </ul>
  <address class="contact">218 W. Larchmont Street<br>Suite 300, Alderton, WI 53210<br>P.&nbsp; 414-555-0148 <span class="contact-label">F.</span>&nbsp; 414-555-0192</address>
</section>

<!-- Variation 3: six attorneys with office locations -->
<section class="letterhead letterhead--offices">
  <header class="brand"><span class="brand-dot"></span><span class="brand-name">Halvorsen &amp; Brandt LLP</span></header>
  <p class="salutation">Dear Mr. Smith,</p>
  <div class="body-copy">
    <p>Lorem ipsum dolor sit amet, consectetur adipiscing elit. Donec orci purus, luctus vitae dignissim eu, iaculis sed purus. Vivamus faucibus, ipsum nec aliquet viverra, leo mauris condimentum ligula, sit amet sagittis enim ligula quis arcu. Nam egestas tortor id nisi porttitor mattis. In tortor ante, ultricies in suscipit a, tempus non massa. Vivamus et auctor mi. Fusce vel massa nulla. Phasellus nec eros mauris, et scelerisque orci.</p>
    <p>Donec malesuada orci vitae nulla accumsan porta a id massa. Quisque accumsan iaculis magna sit amet fringilla. Maecenas consequat, magna eget tincidunt semper, odio nibh rutrum mi, id feugiat ante nisi eu risus. Vestibulum nunc orci, rhoncus a placerat in, ultricies in mi. Cras mattis varius eros, vel fringilla nisi suscipit eget. Quisque scelerisque sagittis nulla at porttitor.</p>
    <p>Sed id augue vitae urna euismod commodo aliquet a quam. Pellentesque arcu velit, cursus et malesuada ut, consequat et diam. Nullam erat sem, rhoncus id ullamcorper vitae, rhoncus et arcu. In ultricies ultricies nulla, ut rutrum nisi iaculis at. Donec eu magna a metus ornare faucibus. Fusce aliquet faucibus ultricies. Morbi semper, est id tincidunt gravida, sem arcu adipiscing lacus, ac bibendum nulla leo eu purus. Quisque nec diam sed risus consectetur a ccumsan quis quis nibh. Vestibulum id purus lorem.</p>
    <p>It is a long established fact that a reader will be distracted by the readable content of a page when looking at its layout. The point of using Lorem Ipsum is that it has a more-or-less normal distribution of letters, as opposed to using 'Content here, content here', making it look like readable English. Many desktop publishing packages</p>
  </div>
  <p class="closing">Sincerely,</p>
  <div class="signature" role="img" aria-label="Handwritten signature of the attorney"></div>
  <ul class="attorneys">
    <li><span class="star star--gold">*</span>Thomas E. Brandt</li>
    <li><span class="star star--sky">*</span>Walter K. Halvorsen</li>
    <li><span class="star star--orange">*</span>Gregory L. Kowalczyk, SR. Associate</li>
    <li><span class="star star--green">*</span>Laura M. Rourke, SR. Associate</li>
    <li><span class="star star--magenta">*</span>Karen E. Lindqvist,&nbsp; SR. Associate</li>
    <li><span class="star star--navy">*</span>Diane F. Thorsby, Associate</li>
  </ul>
  <address class="contact">218 W. Larchmont Street<br>Suite 300, Alderton, WI 53210<br>P. 414-555-0148 F. 414-555-0192</address>
  <div class="office-rule"></div>
  <ul class="offices">
    <li><span class="star star--gold">*</span> Alderton</li>
    <li><span class="star star--sky">*</span> Kessling</li>
    <li><span class="star star--orange">*</span> Harrow Bay</li>
    <li><span class="star star--green">*</span> Marlowe</li>
    <li><span class="star star--magenta">*</span> Illinois</li>
    <li><span class="star star--navy">*</span> Ohio</li>
  </ul>
</section>

</body>
</html>
```